" Elaboramos soluções para que nossos clientes possam alocar adequadamente os recursos disponíveis (tempo, dinheiro, contatos, produtos, imagem, infra) em ações e iniciativas que tragam resultados efetivos e sustentáveis, alinhados aos seus valores, metas e partes interessadas. Desenvolvemos para eles projetos de investimentos, análises estratégicas, estudos de viabilidade, relatórios de avaliação e monitoramento, referências para formulação de políticas públicas, treinamentos, capacitações, reuniões, oficinas e tantos outras soluções. Acreditamos que o empreendedorismo e a inovação são mecanismos com os quais podemos apoiar o desenvolvimento sustentável local e regional. Nossa essência competitiva reside na proximidade e conexão para com todas as partes interessadas, compromisso com valores éticos e morais, inteligência, assertividade, inovação e aprendizado. Buscamos contato com as necessidades dos clientes desde o primeiro momento, garantindo que a construção das soluções respeite processos de diálogo contínuo. As principais características de nossos serviços são: - Informações e conhecimento confiáveis e aplicáveis; - Ações que gerem valores tangíveis e intangíveis positivos, especialmente no tocante à imagem e à confiabilidade; - Acesso a ideias, relacionamentos e oportunidades únicos; - Inovação. Considerados os elementos acima, é preciso destacar que toda a nossa atuação se dá em sintonia e parceria com cada indivíduo envolvido. Assim, consideramos as pessoas como fundamento e objetivo de nossa atuação. "

```html
<!DOCTYPE html>
<html lang="pt-BR">
<head>
<meta charset="utf-8">
<title>Alvorada Grow — Manual de Identidade Visual</title>
<link rel="stylesheet" href="https://fonts.googleapis.com/css2?family=Montserrat:wght@300;400&display=swap">
<style>
  :root {
    --backdrop: #e8e8e9;
    --paper: #ffffff;
    --paper-shade: #f1f1f3;
    --ink: #6f7f8a;
    --ink-soft: #8d99a2;
    --brand: #4f9fb0;
    --mint: #c6e8cf;
    --aqua: #bfe0ea;
    --lilac: #d9cbe9;
    --blush: #f0d6e8;
    --spine: #b9a8d3;
  }
  * { margin: 0; padding: 0; box-sizing: border-box; }
  html, body { width: 1200px; height: 1200px; overflow: hidden; }
  body {
    background: var(--backdrop);
    font-family: "Montserrat", sans-serif;
    color: var(--ink);
    position: relative;
  }

  /* Cover */
  .cover {
    position: absolute;
    left: 110px; top: 70px;
    width: 460px; height: 460px;
    border-left: 10px solid var(--spine);
    box-shadow: 0 6px 18px rgba(0,0,0,.12);
    overflow: hidden;
  }
  .cover-art {
    position: absolute; inset: 0;
    background: linear-gradient(135deg, var(--mint), var(--aqua) 35%, var(--lilac) 70%, var(--blush));
  }
  .cover-title {
    position: absolute;
    left: 0; right: 0; top: 255px;
    text-align: center;
  }
  .brand-name {
    display: inline-flex; align-items: center; gap: 10px;
    font-weight: 300; font-size: 30px; letter-spacing: .5px;
    color: var(--brand);
  }
  .brand-dot {
    width: 16px; height: 16px; border-radius: 50%;
    background: var(--brand);
  }
  .cover-subtitle {
    margin-top: 14px;
    font-weight: 300; font-size: 13px; letter-spacing: 2px;
    line-height: 1.5; text-transform: uppercase;
    color: var(--ink-soft);
  }

  /* Open spread */
  .spread {
    position: absolute;
    left: 230px; top: 620px;
    width: 880px; height: 440px;
    display: flex;
    box-shadow: 0 6px 18px rgba(0,0,0,.12);
    border-bottom: 4px solid var(--lilac);
  }
  .page {
    position: relative;
    width: 50%; height: 100%;
    background: var(--paper);
    overflow: hidden;
  }
  .page-left {
    background: linear-gradient(90deg, var(--paper) 85%, var(--paper-shade));
  }
  .page-right {
    background: linear-gradient(90deg, var(--paper-shade), var(--paper) 15%);
  }
  .page-art {
    position: absolute;
    top: 0; right: 0;
    width: 170px; height: 100%;
    background: linear-gradient(180deg, var(--aqua), var(--lilac) 60%, var(--blush));
    opacity: .7;
  }

  .credits {
    position: absolute;
    left: 44px; bottom: 44px;
    font-size: 9px; font-weight: 400; line-height: 1.45;
    color: var(--ink);
  }
  .credits p + p { margin-top: 9px; }

  .intro-text {
    position: absolute;
    left: 70px; top: 130px;
    width: 230px;
    font-size: 8.5px; line-height: 1.55;
    text-align: justify;
    color: var(--ink);
  }
</style>
</head>
<body>

<section class="cover">
  <div class="cover-art" role="img" aria-label="Decorative iridescent artwork in mint, aqua, lilac and blush"></div>
  <div class="cover-title">
    <div class="brand-name"><span class="brand-dot"></span>Alvorada Grow</div>
    <div class="cover-subtitle">Manual de<br>Identidade Visual</div>
  </div>
</section>

<section class="spread">
  <div class="page page-left">
    <div class="page-art" role="img" aria-label="Decorative gradient artwork in aqua, lilac and blush"></div>
    <div class="credits">
      <p>Alvorada Grow<br>Manual de Identidade Visual</p>
      <p>Cliente<br>Nome do Cliente</p>
      <p>Projeto de Identidade Visual<br>Logo e Manual de Marca<br>Estúdio e Conceito</p>
      <p>Designers: Lara Mendes,<br>Tiago Rocha e Bruna Alves</p>
    </div>
  </div>
  <div class="page page-right">
    <p class="intro-text">Elaboramos soluções para que nossos clientes possam alocar bem os recursos disponíveis em ações que tragam resultados efetivos e sustentáveis, alinhados aos seus valores e metas. Acreditamos que o empreendedorismo e a inovação apoiam o desenvolvimento local e regional. Buscamos o diálogo contínuo desde o primeiro momento, com proximidade, ética e aprendizado. Consideramos as pessoas como fundamento e objetivo de nossa atuação.</p>
  </div>
</section>

</body>
</html>
```